Business Card for IT company

I need a high tech looking business card using our logo. I prefer something clean and modern.

Target Market(s)

Buyers of IT hardware and software, IT Techies who are key influencers

Industry/Entity Type

Business

```html
<!DOCTYPE html>
<html lang="en">
<head>
<meta charset="utf-8">
<title>Kelvra Consulting – Business Card</title>
<link rel="stylesheet" href="https://fonts.googleapis.com/css2?family=Fira+Sans:wght@300;400;500;600&display=swap">
<style>
  :root {
    --stage: #2e2e2e;
    --card-dark: #3a3834;
    --card-dark-mark: #46443f;
    --card-light: #ffffff;
    --ink: #333333;
    --ink-soft: #555555;
    --rule: #4a4a4a;
    --accent: #6ab42d;
    --white: #ffffff;
    --muted-light: #b9b9b9;
  }
  * { box-sizing: border-box; margin: 0; padding: 0; }
  html, body {
    width: 1200px; height: 900px; overflow: hidden;
    background: var(--stage);
    font-family: "Fira Sans", Arial, sans-serif;
  }
  .canvas { position: relative; width: 1200px; height: 900px; }

  .card {
    position: absolute; top: 308px; width: 514px; height: 285px; overflow: hidden;
  }
  /* back */
  .card-back { left: 73px; background: var(--card-dark); }
  .back-mark {
    position: absolute; left: 4px; top: 52px;
    font-size: 148px; font-weight: 600; letter-spacing: -4px; line-height: 1;
    color: var(--card-dark-mark); white-space: nowrap;
  }
  .back-brand { position: absolute; right: 30px; top: 202px; text-align: left; }
  .back-brand .brand-name {
    font-size: 38px; font-weight: 600; color: var(--white); line-height: 1; letter-spacing: -0.5px;
  }
  .back-brand .brand-sub {
    margin-top: 6px; font-size: 11px; font-weight: 300; letter-spacing: 6px; color: var(--muted-light);
  }

  /* front */
  .card-front { left: 615px; background: var(--card-light); }
  .front-brand { position: absolute; left: 29px; top: 24px; }
  .front-brand .brand-name {
    font-size: 56px; font-weight: 600; color: var(--ink); line-height: 1; letter-spacing: -1px;
  }
  .front-brand .brand-sub {
    margin-top: 8px; font-size: 14px; font-weight: 300; letter-spacing: 8.6px; color: var(--ink-soft);
  }
  .person { position: absolute; left: 29px; top: 145px; color: var(--ink); }
  .person-name { font-size: 22px; font-weight: 400; }
  .person-role { font-size: 15px; font-weight: 400; margin-top: 1px; }
  .divider {
    position: absolute; left: 0; right: 0; top: 199px; height: 2px; background: var(--rule);
  }
  .contact-list {
    position: absolute; top: 212px; list-style: none;
    font-size: 14px; line-height: 17.5px; color: var(--ink); white-space: nowrap;
  }
  .contact-list.left { left: 30px; }
  .contact-list.right { left: 306px; }
  .contact-list li { display: flex; align-items: flex-start; }
  .contact-list .icon { width: 14px; flex: none; display: flex; justify-content: flex-start; padding-top: 3px; }
  .contact-list .icon svg { fill: var(--accent); }
  .contact-list .indent { padding-left: 14px; }
  .accent { color: var(--accent); }
</style>
</head>
<body>
<main class="canvas">

  <section class="card card-back" aria-label="Card back">
    <div class="back-mark" aria-hidden="true">KELVRA</div>
    <div class="back-brand">
      <div class="brand-name">KELVRA</div>
      <div class="brand-sub">CONSULTING</div>
    </div>
  </section>

  <section class="card card-front" aria-label="Card front">
    <div class="front-brand">
      <div class="brand-name">KELVRA</div>
      <div class="brand-sub">CONSULTING</div>
    </div>

    <div class="person">
      <div class="person-name">Marcus Ellery</div>
      <div class="person-role">managing director</div>
    </div>

    <div class="divider"></div>

    <ul class="contact-list left">
      <li><span class="icon"><svg width="8" height="11" viewBox="0 0 8 11"><path d="M1 0h6a1 1 0 0 1 1 1v9a1 1 0 0 1-1 1H1a1 1 0 0 1-1-1V1a1 1 0 0 1 1-1zm0.6 1.4v7h4.8v-7z"/></svg></span>212 574 30 61</li>
      <li><span class="icon"><svg width="11" height="10" viewBox="0 0 11 10"><path d="M3 0h5v3H3zM0 3.5h11v4H9V10H2V7.5H0zM3 6.5v2.5h5V6.5z"/></svg></span>212 574 30 62</li>
      <li><span class="icon"><svg width="11" height="8" viewBox="0 0 11 8"><path d="M0 0h11v1L5.5 4.2 0 1zM0 2.2l5.5 3.2L11 2.2V8H0z"/></svg></span>info@kelvra.com</li>
    </ul>

    <ul class="contact-list right">
      <li><span class="icon"><svg width="9" height="12" viewBox="0 0 9 12"><path d="M4.5 0A4.5 4.5 0 0 1 9 4.5C9 7.5 4.5 12 4.5 12S0 7.5 0 4.5A4.5 4.5 0 0 1 4.5 0zm0 2.6a1.9 1.9 0 1 0 0 3.8 1.9 1.9 0 0 0 0-3.8z"/></svg></span>48 Harlow Lane</li>
      <li class="indent">Brookfield, New York 12408</li>
      <li><span class="icon"><svg width="10" height="10" viewBox="0 0 10 10"><circle cx="5" cy="5" r="4.4" fill="none" stroke="#6ab42d" stroke-width="1.2"/><path d="M0.6 5h8.8M5 0.6v8.8" stroke="#6ab42d" stroke-width="1"/><ellipse cx="5" cy="5" rx="2" ry="4.4" fill="none" stroke="#6ab42d" stroke-width="1"/></svg></span>www.<span class="accent">kelvra</span>.com</li>
    </ul>
  </section>

</main>
</body>
</html>
```